Verdano Harvest - Stationery Design Project

We need a stationary for our business. We grow roots and fruits in Central and South America, we import and distribute in FL, USA. We do fresh and frozen products.

Target Market(s)

Small and big supermarkets, wholesalers, traders, distributors, etc

Industry/Entity Type

Business

```html
<!DOCTYPE html>
<html lang="en">
<head>
<meta charset="utf-8">
<title>Verdano Harvest – Business Card</title>
<link href="https://fonts.googleapis.com/css2?family=Karla:wght@400;500;700&display=swap" rel="stylesheet">
<style>
  :root {
    --canvas-bg: #e4e4e4;
    --card-bg: #ffffff;
    --brand-orange: #ee8511;
    --brand-green: #5a6b34;
    --text-grey: #4d4d4d;
    --card-shadow: 0 10px 28px rgba(0,0,0,0.18);
  }
  * { margin: 0; padding: 0; box-sizing: border-box; }
  html, body {
    width: 1200px;
    height: 960px;
    overflow: hidden;
    background: var(--canvas-bg);
    font-family: "Karla", Arial, sans-serif;
  }
  .canvas {
    width: 1200px;
    height: 960px;
    display: flex;
    flex-direction: column;
    align-items: center;
    justify-content: center;
    gap: 44px;
  }
  .card {
    position: relative;
    width: 740px;
    height: 423px;
    background: var(--card-bg);
    border-radius: 40px;
    box-shadow: var(--card-shadow);
    overflow: hidden;
  }

  /* Front */
  .card-front .person {
    position: absolute;
    left: 70px;
    top: 70px;
  }
  .person-name {
    font-size: 30px;
    font-weight: 500;
    color: var(--brand-orange);
    line-height: 1.1;
  }
  .person-name .first { font-weight: 700; }
  .person-role {
    margin-top: 10px;
    font-size: 17px;
    color: var(--brand-green);
  }
  .contact-list {
    position: absolute;
    left: 70px;
    bottom: 58px;
    list-style: none;
    font-size: 19px;
    line-height: 30px;
    color: var(--text-grey);
    letter-spacing: 0.3px;
  }
  .brand-lockup {
    position: absolute;
    right: 56px;
    bottom: 80px;
    display: flex;
    align-items: center;
    gap: 12px;
  }
  .brand-dot {
    width: 16px;
    height: 16px;
    border-radius: 50%;
    background: var(--brand-green);
  }
  .brand-name {
    font-size: 30px;
    font-weight: 700;
    color: var(--brand-green);
  }
  .card-band {
    position: absolute;
    left: 0;
    bottom: 0;
    width: 100%;
    height: 26px;
    display: block;
  }

  /* Back */
  .card-back {
    display: flex;
    flex-direction: column;
    align-items: center;
    justify-content: center;
    gap: 18px;
  }
  .back-lockup {
    display: flex;
    align-items: center;
    gap: 18px;
  }
  .back-lockup .brand-dot {
    width: 34px;
    height: 34px;
  }
  .back-lockup .brand-name {
    font-size: 48px;
  }
  .back-website {
    font-size: 18px;
    font-weight: 500;
    color: var(--brand-orange);
    letter-spacing: 0.5px;
  }
</style>
</head>
<body>
<main class="canvas">

  <section class="card card-front" aria-label="Business card front">
    <div class="person">
      <p class="person-name"><span class="first">Mateo</span> Rivera</p>
      <p class="person-role">CEO</p>
    </div>

    <ul class="contact-list">
      <li>Address,</li>
      <li>Country-XXXXX</li>
      <li>Tel:&nbsp; XXXX XXX XXX</li>
      <li>info@verdanoharvest.co</li>
      <li>www.verdanoharvest.co</li>
    </ul>

    <div class="brand-lockup">
      <span class="brand-dot"></span>
      <span class="brand-name">Verdano Harvest</span>
    </div>

    <svg class="card-band" viewBox="0 0 740 26" preserveAspectRatio="none" aria-hidden="true">
      <polygon points="0,0 250,0 238,26 0,26" fill="var(--brand-orange)"/>
      <polygon points="258,0 740,0 740,26 246,26" fill="var(--brand-green)"/>
    </svg>
  </section>

  <section class="card card-back" aria-label="Business card back">
    <div class="back-lockup">
      <span class="brand-dot"></span>
      <span class="brand-name">Verdano Harvest</span>
    </div>
    <p class="back-website">www.verdanoharvest.co</p>
  </section>

</main>
</body>
</html>
```